Business Card Design

Business Card for professional consulting firm working with large financial institutions.

Target Market(s)

Executive buyers

Industry/Entity Type

Banking

Contact Information for Business Card

Mild creativity wanted. Not boring, but do elaborate artwork.

Font styles to use
Serif
Sans Serif

Colors

Designer to choose colors to be used in the design.

Requirements
Must have
• Standard business card features - company name, individual name, telephone, website, email, locations.
Nice to have
• Two colors
Should not have
• too many colors, fancy printing, cartoons.

```html
<!DOCTYPE html>
<html lang="en">
<head>
<meta charset="utf-8">
<title>k7advisors — Business Card</title>
<link href="https://fonts.googleapis.com/css2?family=Tinos:wght@400&family=Open+Sans:wght@400&display=swap" rel="stylesheet">
<style>
  :root {
    --backdrop: #2b2d31;
    --card: #ffffff;
    --texture-light: #ffffff;
    --texture-shade: #eeeeee;
    --ink: #1c1c1c;
    --ink-soft: #555555;
    --rule: #b5b5b5;
    --band: #c8c8c8;
    --icon: #8e8e8e;
  }
  * { box-sizing: border-box; margin: 0; padding: 0; }
  html, body { width: 1200px; height: 1200px; overflow: hidden; }
  body {
    background: var(--backdrop);
    display: flex;
    flex-direction: column;
    align-items: center;
    justify-content: center;
    gap: 52px;
  }
  .card {
    position: relative;
    width: 900px;
    height: 514px;
    background: var(--card);
    border-radius: 34px;
    overflow: hidden;
  }
  .card-texture {
    position: absolute;
    inset: 0;
    background: linear-gradient(135deg, var(--texture-shade) 0%, var(--texture-light) 45%, var(--texture-light) 60%, var(--texture-shade) 100%);
  }
  .brand-name {
    font-family: "Tinos", serif;
    font-weight: 400;
    color: var(--ink);
    position: absolute;
    white-space: nowrap;
  }

  /* Front side */
  .card-front .brand-name {
    left: 70px;
    top: 96px;
    font-size: 50px;
  }
  .card-front .divider {
    position: absolute;
    left: 408px;
    top: 120px;
    width: 2px;
    height: 300px;
    background: var(--rule);
  }
  .holder {
    position: absolute;
    left: 456px;
    top: 150px;
  }
  .holder-name {
    font-family: "Tinos", serif;
    font-size: 46px;
    letter-spacing: 1px;
    color: var(--ink);
    line-height: 1;
  }
  .holder-role {
    font-family: "Open Sans", sans-serif;
    font-size: 22px;
    color: var(--ink-soft);
    margin-top: 6px;
    padding-bottom: 10px;
    border-bottom: 2px solid var(--rule);
    width: 240px;
  }
  .contact-list {
    list-style: none;
    margin-top: 14px;
    font-family: "Open Sans", sans-serif;
    font-size: 24px;
    color: var(--ink);
    line-height: 1.45;
  }
  .contact-list li { display: flex; align-items: center; gap: 12px; }
  .contact-list svg { width: 18px; height: 18px; flex: none; }

  /* Back side */
  .card-back .brand-name {
    left: 0;
    right: 0;
    top: 170px;
    text-align: center;
    font-size: 72px;
  }
  .address-band {
    position: absolute;
    left: 0;
    right: 0;
    top: 392px;
    height: 56px;
    background: var(--band);
    display: flex;
    align-items: center;
    justify-content: center;
    font-family: "Open Sans", sans-serif;
    font-size: 22px;
    color: var(--ink);
  }
</style>
</head>
<body>

  <section class="card card-front">
    <div class="card-texture" role="img" aria-label="Subtle quilted diamond texture in white and light grey"></div>
    <span class="brand-name">k7advisors</span>
    <div class="divider"></div>
    <div class="holder">
      <h1 class="holder-name">DANIEL HARPER</h1>
      <p class="holder-role">General Manager</p>
      <ul class="contact-list">
        <li>
          <svg viewBox="0 0 20 20" aria-hidden="true"><path fill="var(--icon)" d="M5 2c1 0 2 3 2 4s-1 1.5-1 2c0 1 3 5 5 5 .6 0 1-1 2-1s4 1 4 2-1 4-3 4C8 18 2 12 2 5c0-2 2-3 3-3z"/></svg>
          312.555.0148
        </li>
        <li>
          <svg viewBox="0 0 20 20" aria-hidden="true"><rect x="2" y="4" width="16" height="12" rx="2" fill="var(--icon)"/><path d="M3 5l7 6 7-6" fill="none" stroke="#fff" stroke-width="1.5"/></svg>
          harper@k7advisors.com
        </li>
        <li>
          <svg viewBox="0 0 20 20" aria-hidden="true"><circle cx="10" cy="10" r="8" fill="var(--icon)"/><path d="M2 10h16M10 2c-4 4-4 12 0 16M10 2c4 4 4 12 0 16" fill="none" stroke="#fff" stroke-width="1.2"/></svg>
          www.k7advisors.com
        </li>
      </ul>
    </div>
  </section>

  <section class="card card-back">
    <div class="card-texture" role="img" aria-label="Subtle quilted diamond texture in white and light grey"></div>
    <span class="brand-name">k7advisors</span>
    <div class="address-band">1820 Meridian Ave, Lexington, KY, 40507</div>
  </section>

</body>
</html>
```